Organic rose water based skincare line in need of product label and packaging design

We are looking for a simple, clean, modern labeling and packaging design for 2 of our products. Our brand's demographic is upscale females ages 20-40. We want our packaging to be very minimalistic, and instagramable.

Product #1: Rose water facial spray "Lumi Mist"
Product #2: Rose water facial toner "Velvet Hush Hour"

Please see attached images for our current logo and label design. We have also added some images that inspire our branding.

Target Market(s)

trendy woman ages 20-40

Industry/Entity Type

Skin Care Product

Font styles to use
Serif
Sans Serif

Colors

Designer to choose only greyscale colors for use in the design.

Requirements
Must have
• Must have our logo, bottle size, product name on front and how to use and ingredient on the back. Please see project description and attached images for more information.
Should not have
• Too much going on or too many colors.

```html
<!DOCTYPE html>
<html lang="en">
<head>
<meta charset="utf-8">
<title>Lumi Mist – label</title>
<link rel="stylesheet" href="https://fonts.googleapis.com/css2?family=Bebas+Neue&family=Raleway:wght@400;500;700&display=swap">
<style>
  :root {
    --ink: #000000;
    --paper: #ffffff;
    --rule: #9a9a9a;
    --art-tone: #e6e6e6;
  }
  * { margin: 0; padding: 0; box-sizing: border-box; }
  html, body { width: 1200px; height: 1180px; overflow: hidden; background: var(--paper); }
  .label {
    position: relative;
    width: 1200px;
    height: 1180px;
    background: var(--paper);
    color: var(--ink);
    font-family: "Raleway", sans-serif;
  }
  .panel { position: absolute; top: 0; height: 1180px; width: 597px; }
  .panel--front { left: 0; }
  .panel--back { left: 598px; width: 602px; }
  .divider {
    position: absolute; left: 597px; top: 74px;
    width: 1px; height: 1024px; background: var(--rule);
  }
  .centered { position: absolute; left: 0; right: 0; text-align: center; }

  .brand-name {
    top: 150px;
    font-family: "Raleway", sans-serif;
    font-weight: 500;
    font-size: 44px;
    line-height: 46px;
    letter-spacing: -0.5px;
    text-transform: lowercase;
  }
  .product-name {
    top: 340px;
    font-family: "Bebas Neue", sans-serif;
    font-size: 108px;
    line-height: 108px;
    letter-spacing: 1px;
  }
  .product-type {
    position: absolute; left: 179px; top: 446px;
    width: 201px; height: 28px; border-radius: 14px;
    background: var(--ink); color: var(--paper);
    font-size: 19px; line-height: 28px; text-align: center;
  }
  .product-desc { top: 497px; font-size: 21px; }
  .volume { top: 1045px; font-size: 20px; }

  .rose-art {
    position: absolute;
    background: var(--art-tone);
    border-radius: 6px;
  }
  .rose-art--front { left: 213px; top: 713px; width: 145px; height: 253px; }
  .rose-art--back { left: 238px; top: 148px; width: 146px; height: 253px; }

  .section-title { font-weight: 700; font-size: 20px; letter-spacing: 0.3px; }
  .usage-title { top: 580px; }
  .usage-text { top: 628px; font-size: 21px; line-height: 26px; }
  .benefits-title { top: 800px; }
  .benefits {
    top: 852px; list-style: none;
    font-size: 20px; line-height: 32.7px;
  }
</style>
</head>
<body>
<main class="label">
  <section class="panel panel--front">
    <div class="centered brand-name">petal<br>atelier</div>
    <h1 class="centered product-name">LUMI MIST</h1>
    <div class="product-type">Organic rosewater</div>
    <p class="centered product-desc">Hydrating mist</p>
    <div class="rose-art rose-art--front" role="img" aria-label="Line drawing of a single long-stemmed rose with leaves"></div>
    <p class="centered volume">2 oz/60ml</p>
  </section>

  <div class="divider"></div>

  <section class="panel panel--back">
    <div class="rose-art rose-art--back" role="img" aria-label="Line drawing of a single long-stemmed rose with leaves"></div>
    <h2 class="centered section-title usage-title">TO USE</h2>
    <p class="centered usage-text">Mist over<br>face + body + hair<br>as desired for hydration</p>
    <h2 class="centered section-title benefits-title">ORGANIC ROSE WATER</h2>
    <ul class="centered benefits">
      <li>Hydrates</li>
      <li>fights acne</li>
      <li>mantains skin’s pH</li>
      <li>strengthens skin cells</li>
      <li>prevents fine lines &amp; wrinkles</li>
    </ul>
  </section>
</main>
</body>
</html>
```